Insurance Company Website Design

We are working with an insurance company. They sell home, auto, commercial, and health insurance. We like the "get a quote" in the banner of https://www.plovendi.com and https://www.quorvelix.com.

Some sites to use for content/competitors and inspiration:
https://copperhavenins.com
https://kimbrantuskinsurance.com
https://rtwellsinsurance.com
https://www.insuranceformervane.com
https://www.plovendi.com
https://www.quorvelix.com

Thank you for taking the time to consider designing a website for us. We are web developers based in Stockton, CA, USA. Most of our projects go through the same process. Understanding this process may help you win a project with us. We custom-code all of our websites in-house. We don’t have any requirements as to what tools you use for your design, but we ask that you follow these guidelines.

IMAGES:
If you use any images or icons in the design, we ask that you have a link to the asset so we can purchase the image/icon. Most of the designs we submit do not have the customer’s images on them unless they have some great images. Be creative; show us the feeling you are trying to portray with your image choices. Use any royalty-free site you choose. We subscribe to Zentrik and mainly use their images, but we can purchase images outside of Zentrik. PLEASE NOTE: we will not submit designs to clients with watermarks on the images.

FONTS:
We ask that you identify the fonts you’re using in the design. This can be done in a message if you want. We typically use Vumbra Fonts and Zentrik Fonts.

CONTENT:
We're always open to different content and ideas. We often submit designs with stock images so the client can see our vision. We typically take pictures after the website launch to use their images with our vision. Lorem Ipsum is fine for paragraphs, but we ask that you make the Headers with correct English. We want to be able to show the vision and identify the sections of the website.

INSPIRATION:
We typically add a couple of links in the brief of websites we like to help you get started in your design.

REVISIONS:
We do not often ask for revisions of the designs unless we see something in the design that may not appeal to the client. If there are slight changes that we want to make, we do that in the development process.

FEEDBACK:
We rarely give feedback on designs during the design process. We are working on many website projects and do not have the time to provide feedback. We usually respond if your request is well thought out and asks specific questions, but a note asking “feedback, please” usually goes unanswered.

```html
<!DOCTYPE html>
<html lang="en">
<head>
<meta charset="utf-8">
<title>Canopia Insurance</title>
<link href="https://fonts.googleapis.com/css2?family=Poppins:wght@300;400;500;600;700&display=swap" rel="stylesheet">
<style>
:root{
  --blue:#1766c2;
  --blue-deep:#0f58b3;
  --blue-light:#2f86d6;
  --title-blue:#1a5fb4;
  --ink:#111;
  --text:#666;
  --muted:#8a8a8a;
  --tint:#eef4fc;
  --footer:#edf1fb;
  --card:#f4f4f4;
  --white:#fff;
  --star:#f5b81c;
}
*{margin:0;padding:0;box-sizing:border-box}
html,body{width:1200px;height:4161px;overflow:hidden}
body{font-family:'Poppins',sans-serif;color:var(--ink);background:var(--white);position:relative}
.abs{position:absolute}

/* hero */
.hero-bg{position:absolute;left:0;top:0;width:1200px;height:700px}
.nav-logo{left:89px;top:42px;font-size:34px;font-weight:400;color:var(--white);display:flex;align-items:center;gap:10px}
.nav-logo .dot{width:14px;height:14px;border-radius:50%;background:var(--white)}
.nav{left:318px;top:58px;display:flex;gap:0;font-size:13px;color:var(--white)}
.nav a{color:var(--white);text-decoration:none;position:absolute;white-space:nowrap}
.hero-kicker{left:81px;top:152px;font-size:27px;font-weight:500;color:var(--white)}
.hero-title{left:81px;top:196px;font-size:42px;font-weight:600;line-height:58px;color:var(--white)}
.hero-photo{left:520px;top:145px;width:597px;height:501px}

.quote-card{left:84px;top:339px;width:333px;height:396px;background:var(--white);border-radius:4px;box-shadow:0 4px 18px rgba(0,0,0,.12);text-align:center}
.quote-card h2{margin-top:26px;font-size:28px;font-weight:500;color:var(--blue)}
.quote-card hr{border:0;border-top:1px solid #eee;margin:14px 0 0}
.field{position:absolute;left:42px;width:245px;height:48px;background:#f2f2f2;border-radius:4px;font-size:13px;color:#999;text-align:left;padding:15px 11px}
.field .caret{position:absolute;right:16px;top:22px;border:5px solid transparent;border-top-color:#aaa}
.btn{position:absolute;display:flex;align-items:center;justify-content:center;background:var(--blue-deep);color:var(--white);border-radius:24px;font-weight:500}
.quote-card .btn{left:87px;top:284px;width:157px;height:47px;font-size:16px}
.quote-card .save{position:absolute;left:0;right:0;top:350px;font-size:11px;color:var(--muted)}

/* services */
.sec-title{left:0;width:1200px;text-align:center;font-weight:600}
.services-title{top:744px;font-size:26px}
.services-lead{top:804px;left:225px;width:750px;text-align:center;font-size:17px;line-height:25px;color:var(--text)}
.svc{top:908px;width:333px;height:239px;background:var(--card);border-radius:12px;padding:44px 26px}
.svc.active{background:var(--white);box-shadow:0 8px 24px rgba(0,0,0,.12)}
.svc h3{font-size:24px;font-weight:500;margin-top:14px}
.svc p{font-size:13px;line-height:21px;color:var(--text);margin-top:10px;width:240px}

/* about */
.about{left:0;top:1239px;width:1200px;height:471px;background:var(--tint)}
.about h2{position:absolute;left:173px;top:122px;font-size:30px;font-weight:600}
.about p{position:absolute;left:173px;top:180px;width:370px;font-size:13px;line-height:20px;color:var(--text)}
.about .btn{left:173px;top:308px;width:158px;height:41px;font-size:15px;font-weight:600;background:#2a74c8}
.about-art{left:654px;top:98px;width:412px;height:278px;border-radius:40px}

/* features */
.kicker{top:1800px;font-size:16px;font-weight:500;letter-spacing:3px}
.feat-title{top:1833px;font-size:34px}
.feat{width:283px;height:299px;background:var(--white);border-radius:14px;box-shadow:0 4px 20px rgba(0,0,0,.06);text-align:center;padding-top:48px}
.feat .ico{width:77px;height:77px;border-radius:50%;background:#2c7cd2;margin:0 auto;display:flex;align-items:center;justify-content:center}
.feat h3{font-size:17px;font-weight:500;margin-top:28px}
.feat p{font-size:13.5px;line-height:20px;color:var(--text);width:190px;margin:4px auto 0}

/* testimonials */
.testi{left:0;top:2676px;width:1200px;height:462px;background:var(--tint)}
.blue-title{left:0;width:1200px;text-align:center;font-size:34px;font-weight:600;color:var(--title-blue)}
.tcard{top:2859px;width:246px;height:181px;background:var(--white);box-shadow:0 2px 10px rgba(0,0,0,.06);text-align:center;padding-top:32px}
.tcard h4{font-size:13px;font-weight:500}
.tcard .stars{color:var(--star);font-size:9px;letter-spacing:2px;margin-top:4px}
.tcard p{font-size:9.5px;line-height:16px;color:var(--muted);width:190px;margin:8px auto 0}
.arrow{width:22px;height:22px;border-radius:50%;display:flex;align-items:center;justify-content:center}

/* news */
.news-img{background:linear-gradient(135deg,#b9c9dc,#e8eef5 45%,#8fa6c2)}
.news-big{left:84px;top:3311px;width:506px;height:387px;background:var(--white);border-bottom:2px solid var(--blue)}
.news-big .news-img{height:218px}
.news-big .date{position:absolute;left:29px;top:232px;font-size:9.5px;color:var(--blue)}
.news-big h3{position:absolute;left:27px;top:254px;font-size:22px;font-weight:400;color:#333}
.news-big p{position:absolute;left:29px;top:296px;font-size:9.5px;line-height:15px;color:var(--muted);width:300px}
.news-big .more{position:absolute;left:29px;top:358px;font-size:9.5px;font-weight:600;color:var(--blue);border-bottom:1px solid var(--blue)}
.news-sm{left:607px;width:506px;height:121px;background:var(--white);border-bottom:2px solid var(--blue);box-shadow:0 2px 10px rgba(0,0,0,.05)}
.news-sm .news-img{position:absolute;left:0;top:0;width:157px;height:119px}
.news-sm h3{position:absolute;left:175px;top:16px;font-size:20px;font-weight:400;line-height:30px;color:#444}
.news-sm .date{position:absolute;left:177px;top:94px;font-size:9.5px;color:var(--blue)}

/* footer */
.footer{left:0;top:3763px;width:1200px;height:352px;background:var(--footer)}
.f-logo{left:157px;top:62px;font-size:36px;color:var(--blue);display:flex;align-items:center;gap:10px}
.f-logo .dot{width:14px;height:14px;border-radius:50%;background:var(--blue)}
.f-addr{left:154px;top:134px;font-size:13.5px;line-height:20px;font-weight:500}
.f-contact{left:154px;font-size:13.5px;font-weight:500;display:flex;align-items:center;gap:10px}
.f-col h4{font-size:16px;font-weight:600}
.f-col ul{list-style:none;margin-top:14px}
.f-col li{font-size:11.5px;line-height:24px}
.f-input{left:783px;top:144px;width:262px;height:45px;background:var(--white);border-radius:4px;font-size:13px;color:#777;padding:13px 14px}
.social{left:783px;top:268px;display:flex;gap:10px;font-size:11px;font-weight:500;color:var(--blue)}
.bar{left:0;top:4115px;width:1200px;height:46px;background:var(--blue-deep);color:var(--white);font-size:11.5px}
</style>
</head>
<body>

<!-- Hero -->
<svg class="hero-bg" viewBox="0 0 1200 700" aria-hidden="true">
  <defs>
    <linearGradient id="heroGrad" x1="0" y1="0" x2="1" y2="1">
      <stop offset="0" stop-color="#0f5db8"/>
      <stop offset="1" stop-color="#2f86d6"/>
    </linearGradient>
  </defs>
  <path d="M0 0H1200V640C1080 575 920 520 720 525C560 530 420 560 300 600C180 640 90 650 0 680Z" fill="url(#heroGrad)"/>
</svg>

<div class="abs nav-logo"><span class="dot"></span>Canopia</div>
<nav class="abs nav" style="left:0;top:58px">
  <a style="left:318px">Insurance</a>
  <a style="left:413px">Get a Quote</a>
  <a style="left:521px">Investment</a>
  <a style="left:625px">Find a Agent</a>
  <a style="left:738px">Claim</a>
  <a style="left:806px">Contact Us</a>
</nav>
<svg class="abs" style="left:1007px;top:58px" width="18" height="18" viewBox="0 0 18 18" aria-label="Search"><circle cx="7.5" cy="7.5" r="5" fill="none" stroke="#fff" stroke-width="2"/><path d="M11 11l5 5" stroke="#fff" stroke-width="2"/></svg>
<svg class="abs" style="left:1080px;top:57px" width="34" height="18" viewBox="0 0 34 18" aria-label="Account"><circle cx="9" cy="5" r="4.5" fill="#fff"/><path d="M1 17c0-5 4-7 8-7s8 2 8 7z" fill="#fff"/><path d="M23 8h7l-3.5 4z" fill="#fff"/></svg>

<div class="abs hero-kicker">Security That Spans Horizons,</div>
<div class="abs hero-title">Experience The Strength Of<br>Our Canopia Coverage</div>

<svg class="abs hero-photo" viewBox="0 0 597 501" role="img" aria-label="Photo of a smiling family sitting together on a living room floor">
  <defs>
    <linearGradient id="photoGrad" x1="0" y1="0" x2="1" y2="1">
      <stop offset="0" stop-color="#e9e2d8"/>
      <stop offset=".5" stop-color="#c9b6a0"/>
      <stop offset="1" stop-color="#6f8fb6"/>
    </linearGradient>
  </defs>
  <path d="M190 30C240 -10 330 10 400 40C480 70 597 100 597 250C597 330 540 380 450 370C380 365 340 380 300 440C260 500 200 520 180 430C165 370 110 360 50 340C-10 320 -10 250 40 220C100 185 140 70 190 30Z" fill="url(#photoGrad)"/>
</svg>

<section class="abs quote-card">
  <h2>Start a Quote</h2>
  <hr>
  <div class="field" style="top:105px">Product<span class="caret"></span></div>
  <div class="field" style="top:192px">Zip Code</div>
  <div class="btn">Get a Quote</div>
  <div class="save">Continue a Save Quote</div>
</section>

<!-- Our services -->
<h2 class="abs sec-title services-title">Our Services</h2>
<p class="abs services-lead">Lorem Ipsum is simply dummy text of the printing and typesetting industry. Lorem Ipsum has been the industry's standard dummy text ever since the 1500s,</p>

<div class="abs svc" style="left:84px">
  <svg width="60" height="52" viewBox="0 0 60 52" aria-hidden="true"><circle cx="42" cy="34" r="16" fill="#bde6f3"/><path d="M24 3l5 4 6-1 1 6 5 4-3 5 1 6-6 1-3 5-6-2-6 2-3-5-6-1 1-6-3-5 5-4 1-6 6 1z" fill="none" stroke="#222" stroke-width="2"/><path d="M16 22l6 6 11-12" fill="none" stroke="#222" stroke-width="2.2"/></svg>
  <h3>Services</h3>
  <p>Lorem Ipsum is simply dummy text of the typesetting industry.</p>
</div>
<div class="abs svc active" style="left:433px">
  <svg width="60" height="52" viewBox="0 0 60 52" aria-hidden="true"><circle cx="42" cy="34" r="16" fill="#bde6f3"/><path d="M24 3l5 4 6-1 1 6 5 4-3 5 1 6-6 1-3 5-6-2-6 2-3-5-6-1 1-6-3-5 5-4 1-6 6 1z" fill="none" stroke="#222" stroke-width="2"/><path d="M16 22l6 6 11-12" fill="none" stroke="#222" stroke-width="2.2"/></svg>
  <h3>Services</h3>
  <p>Lorem Ipsum is simply dummy text of the typesetting industry.</p>
</div>
<div class="abs svc" style="left:783px">
  <svg width="60" height="52" viewBox="0 0 60 52" aria-hidden="true"><circle cx="42" cy="34" r="16" fill="#bde6f3"/><path d="M24 3l5 4 6-1 1 6 5 4-3 5 1 6-6 1-3 5-6-2-6 2-3-5-6-1 1-6-3-5 5-4 1-6 6 1z" fill="none" stroke="#222" stroke-width="2"/><path d="M16 22l6 6 11-12" fill="none" stroke="#222" stroke-width="2.2"/></svg>
  <h3>Services</h3>
  <p>Lorem Ipsum is simply dummy text of the typesetting industry.</p>
</div>

<!-- About -->
<section class="abs about">
  <h2>About Us</h2>
  <p>Lorem Ipsum is simply dummy text of the printing and typesetting industry. Lorem Ipsum has been the industry's standard dummy text ever since the 1500s, when an unknown printer took a galley of type and scrambled it to make a type specimen book.</p>
  <div class="btn">SIGN UP</div>
  <div class="abs about-art" role="img" aria-label="Illustration of two people shaking hands in front of an insurance policy on a phone" style="background:linear-gradient(135deg,#cfe0f7,#8fb3ea 60%,#3f6fd1)"></div>
</section>

<!-- Features -->
<div class="abs sec-title kicker">OUR SERVICES</div>
<h2 class="abs sec-title feat-title">Lorem Ipsum is simply dummy text</h2>

<div class="abs feat" style="left:150px;top:1938px"><div class="ico"><svg width="32" height="32" viewBox="0 0 32 32" aria-hidden="true"><path d="M4 15L16 5l12 10v13H20v-9h-8v9H4z" fill="none" stroke="#fff" stroke-width="2.2" stroke-linejoin="round"/></svg></div><h3>Lorem Ipsum</h3><p>Lorem Ipsum is simply dummy text of the printing and typesetting industry since the 1500s</p></div>
<div class="abs feat" style="left:459px;top:1938px"><div class="ico"><svg width="32" height="32" viewBox="0 0 32 32" aria-hidden="true"><path d="M4 15L16 5l12 10v13H20v-9h-8v9H4z" fill="none" stroke="#fff" stroke-width="2.2" stroke-linejoin="round"/></svg></div><h3>Lorem Ipsum</h3><p>Lorem Ipsum is simply dummy text of the printing and typesetting industry since the 1500s</p></div>
<div class="abs feat" style="left:769px;top:1938px"><div class="ico"><svg width="32" height="32" viewBox="0 0 32 32" aria-hidden="true"><path d="M4 15L16 5l12 10v13H20v-9h-8v9H4z" fill="none" stroke="#fff" stroke-width="2.2" stroke-linejoin="round"/></svg></div><h3>Lorem Ipsum</h3><p>Lorem Ipsum is simply dummy text of the printing and typesetting industry since the 1500s</p></div>
<div class="abs feat" style="left:150px;top:2269px"><div class="ico"><svg width="32" height="32" viewBox="0 0 32 32" aria-hidden="true"><path d="M4 15L16 5l12 10v13H20v-9h-8v9H4z" fill="none" stroke="#fff" stroke-width="2.2" stroke-linejoin="round"/></svg></div><h3>Lorem Ipsum</h3><p>Lorem Ipsum is simply dummy text of the printing and typesetting industry since the 1500s</p></div>
<div class="abs feat" style="left:459px;top:2269px"><div class="ico"><svg width="32" height="32" viewBox="0 0 32 32" aria-hidden="true"><path d="M4 15L16 5l12 10v13H20v-9h-8v9H4z" fill="none" stroke="#fff" stroke-width="2.2" stroke-linejoin="round"/></svg></div><h3>Lorem Ipsum</h3><p>Lorem Ipsum is simply dummy text of the printing and typesetting industry since the 1500s</p></div>
<div class="abs feat" style="left:769px;top:2269px"><div class="ico"><svg width="32" height="32" viewBox="0 0 32 32" aria-hidden="true"><path d="M4 15L16 5l12 10v13H20v-9h-8v9H4z" fill="none" stroke="#fff" stroke-width="2.2" stroke-linejoin="round"/></svg></div><h3>Lorem Ipsum</h3><p>Lorem Ipsum is simply dummy text of the printing and typesetting industry since the 1500s</p></div>

<!-- Testimonials -->
<div class="abs testi"></div>
<h2 class="abs blue-title" style="top:2745px">What Our Customers Say</h2>
<div class="abs arrow" style="left:33px;top:2941px;background:#fff;box-shadow:0 1px 4px rgba(0,0,0,.15)"><svg width="10" height="10" viewBox="0 0 10 10" aria-label="Previous"><path d="M9 5H1M4 2L1 5l3 3" fill="none" stroke="#333" stroke-width="1.4"/></svg></div>
<div class="abs arrow" style="left:1145px;top:2941px;background:#3a5fe0"><svg width="10" height="10" viewBox="0 0 10 10" aria-label="Next"><path d="M1 5h8M6 2l3 3-3 3" fill="none" stroke="#fff" stroke-width="1.4"/></svg></div>

<div class="abs tcard" style="left:84px"><h4>John Smith</h4><div class="stars">★★★★★</div><p>Lorem Ipsum is simply dummy text of the typesetting industry. Lorem Ipsum is simply dummy text.</p></div>
<div class="abs tcard" style="left:346px"><h4>John Smith</h4><div class="stars">★★★★★</div><p>Lorem Ipsum is simply dummy text of the typesetting industry. Lorem Ipsum is simply dummy text.</p></div>
<div class="abs tcard" style="left:607px"><h4>John Smith</h4><div class="stars">★★★★★</div><p>Lorem Ipsum is simply dummy text of the typesetting industry. Lorem Ipsum is simply dummy text.</p></div>
<div class="abs tcard" style="left:870px"><h4>John Smith</h4><div class="stars">★★★★★</div><p>Lorem Ipsum is simply dummy text of the typesetting industry. Lorem Ipsum is simply dummy text.</p></div>

<!-- News -->
<h2 class="abs blue-title" style="top:3216px">Latest News</h2>
<article class="abs news-big">
  <div class="news-img" role="img" aria-label="Photo of folded newspapers in a stack"></div>
  <div class="date">Jan 2, 2024</div>
  <h3>Lorem Ipsum is dummy text</h3>
  <p>Lorem Ipsum is dummy text of the typesetting industry. Lorem Ipsum is simply dummy text Lorem Ipsum has been the industry's standard dummy text</p>
  <div class="more">Read More</div>
</article>
<article class="abs news-sm" style="top:3311px"><div class="news-img" role="img" aria-label="Photo of folded newspapers"></div><h3>Lorem Ipsum is<br>dummy text</h3><div class="date">Jan 2, 2024</div></article>
<article class="abs news-sm" style="top:3443px"><div class="news-img" role="img" aria-label="Photo of folded newspapers"></div><h3>Lorem Ipsum is<br>dummy text</h3><div class="date">Jan 2, 2024</div></article>
<article class="abs news-sm" style="top:3576px"><div class="news-img" role="img" aria-label="Photo of folded newspapers"></div><h3>Lorem Ipsum is<br>dummy text</h3><div class="date">Jan 2, 2024</div></article>

<!-- Footer -->
<footer class="abs footer">
  <div class="abs f-logo"><span class="dot"></span>Canopia</div>
  <div class="abs f-addr">58 Larkmere Lane<br>Dovetree, NY 40917</div>
  <div class="abs f-contact" style="top:202px"><svg width="14" height="14" viewBox="0 0 14 14" aria-hidden="true"><path d="M3 1l2.5 3-1.5 1.5c.8 1.8 2 3 3.8 3.8L9.5 7.8 13 10l-1.5 3C6 12.5 1.5 8 1 2.5z" fill="none" stroke="#222" stroke-width="1.2"/></svg>+1 555-013-2468</div>
  <div class="abs f-contact" style="top:237px"><svg width="14" height="12" viewBox="0 0 14 12" aria-hidden="true"><rect x="1" y="1" width="12" height="10" fill="none" stroke="#222" stroke-width="1.2"/><path d="M1 1l6 5 6-5" fill="none" stroke="#222" stroke-width="1.2"/></svg>hello@canopia-mail.com</div>

  <div class="abs f-col" style="left:433px;top:78px"><h4>Link</h4><ul><li>Home</li><li>About</li><li>Services</li><li>Produts</li><li>Blogs</li><li>Career</li></ul></div>
  <div class="abs f-col" style="left:609px;top:78px"><h4>Insurance</h4><ul><li>Auto Insurance</li><li>Home Insurance</li><li>Life Insurance</li><li>Financial Insurance</li></ul></div>
  <div class="abs f-col" style="left:783px;top:78px"><h4>Subscribe to our<br>Newsletter!</h4></div>
  <div class="abs f-input">Email Address</div>
  <div class="abs f-col" style="left:783px;top:233px"><h4>Folow Us On</h4></div>
  <div class="abs social"><span>Pixora</span><span>Frendo</span><span>Zeplo</span></div>
</footer>
<div class="abs bar">
  <span class="abs" style="left:84px;top:15px">© Company- All Rights Reserved</span>
  <span class="abs" style="left:813px;top:15px">Terms and Conditions</span>
  <span class="abs" style="left:960px;top:15px">Privacy Policy</span>
  <span class="abs" style="left:1055px;top:15px">Disclaimer</span>
</div>

</body>
</html>
```